Tractor Trailer & Van Graphics

Develop Graphics for our Vans, Tractor & Trailers, See our website www.quinleyforge.com for brand theme, I included a Brand Style Guide.
On the back doors of the trucks and van we want to highlight our core products, Packaging, Displays, Protective & E commerce, we are very proud of our sustainability efforts as we are 100% solar powered

Target Market(s)

Create Brand identify

Requirements
Must have
• Follow our brand guide line
Nice to have
• Logo. Locations Bullet point on back of trailer
Show Back door options
Show logo on tractor only
trailer show full. 1/2 coverage
Van full wrap

```html
<!DOCTYPE html>
<html lang="en">
<head>
<meta charset="utf-8">
<title>Quinley Forge – Trailer Graphics</title>
<link href="https://fonts.googleapis.com/css2?family=Oswald:wght@500;600;700&family=Roboto:wght@700;900&display=swap" rel="stylesheet">
<style>
  :root {
    --orange: #f07a18;
    --orange-deep: #e85d1e;
    --orange-light: #f6a417;
    --red: #e11b2b;
    --white: #ffffff;
    --ink: #1d1d1f;
    --page: #f1f1f1;
  }
  * { box-sizing: border-box; margin: 0; padding: 0; }
  html, body { width: 990px; height: 1200px; overflow: hidden; }
  body { background: var(--page); position: relative; font-family: "Roboto", Arial, sans-serif; }

  /* Side banner */
  .side-banner {
    position: absolute; left: 57px; top: 60px; width: 876px; height: 170px;
    box-shadow: 0 3px 10px rgba(0,0,0,.15);
  }
  .banner-art { position: absolute; inset: 0; }
  .brand { position: absolute; display: flex; align-items: center; gap: 14px; white-space: nowrap; }
  .side-banner .brand { left: 32px; top: 46px; }
  .brand-mark { width: 44px; height: 44px; background: var(--orange); flex: none; }
  .brand-name {
    font-family: "Oswald", Arial, sans-serif; font-weight: 600;
    font-size: 42px; letter-spacing: 3px; color: var(--red); line-height: 1; white-space: nowrap;
  }
  .side-tagline {
    position: absolute; right: 28px; top: 40px; text-align: right;
    font-family: "Oswald", Arial, sans-serif; font-weight: 600;
    font-size: 24px; line-height: 1.25; color: var(--white); letter-spacing: .5px;
  }

  /* Back doors */
  .door {
    position: absolute; top: 300px; width: 326px; height: 760px; overflow: hidden;
    background: var(--white); box-shadow: 0 3px 10px rgba(0,0,0,.18);
  }
  .door-left { left: 164px; }
  .door-right { left: 500px; }
  .door-field {
    position: absolute; left: 0; top: 0; width: 100%;
    background: radial-gradient(circle at 70% 40%, var(--orange-light) 0%, var(--orange) 60%, var(--orange-deep) 100%);
  }
  .door-left .door-field { height: 590px; }
  .door-right .door-field { height: 760px; }
  .door-art { position: absolute; inset: 0; }

  .door-brand {
    position: absolute; left: 140px; top: 520px;
    transform: rotate(-90deg); transform-origin: 0 0;
    display: flex; align-items: center; gap: 16px; white-space: nowrap;
  }
  .door-brand .brand-name { color: var(--white); font-size: 46px; }
  .door-brand .brand-mark { background: var(--white); width: 40px; height: 40px; }

  .pride-note {
    position: absolute; left: 30px; top: 635px;
    font-family: "Oswald", Arial, sans-serif; font-weight: 600;
    font-size: 21px; line-height: 1.3; color: var(--ink); text-transform: uppercase;
  }

  .products-title {
    position: absolute; left: 22px; top: 58px; color: var(--white);
    font-family: "Oswald", Arial, sans-serif; font-weight: 600; line-height: 1;
  }
  .products-title .big { display: block; font-size: 58px; letter-spacing: 1px; }
  .products-title .small { display: block; font-size: 38px; margin-top: 2px; }

  .product-list { position: absolute; left: 22px; top: 210px; list-style: none; }
  .product-list li {
    display: flex; align-items: center; gap: 16px; height: 62px;
    font-weight: 700; font-size: 32px; color: var(--white); white-space: nowrap;
  }
  .product-icon {
    width: 44px; height: 44px; border-radius: 50%; background: var(--red);
    border: 3px solid var(--white); display: flex; align-items: center; justify-content: center; flex: none;
  }
  .product-icon svg { width: 22px; height: 22px; display: block; }

  .power-claim {
    position: absolute; left: 0; width: 100%; top: 548px; text-align: center;
    font-family: "Oswald", Arial, sans-serif; font-weight: 600; color: var(--ink); line-height: 1;
  }
  .power-claim .lead, .power-claim .tail { display: block; font-size: 36px; }
  .power-claim .figure { display: block; font-size: 118px; font-weight: 700; color: var(--red); margin: 4px 0 2px; letter-spacing: -2px; }
</style>
</head>
<body>

<section class="side-banner" aria-label="Trailer side graphic">
  <svg class="banner-art" viewBox="0 0 876 170" width="876" height="170" aria-hidden="true">
    <defs>
      <linearGradient id="bannerGlow" x1="0" y1="0" x2="1" y2="0">
        <stop offset="0" stop-color="#f6a417"/>
        <stop offset=".55" stop-color="#f07a18"/>
        <stop offset="1" stop-color="#e85d1e"/>
      </linearGradient>
    </defs>
    <rect width="876" height="170" fill="url(#bannerGlow)"/>
    <polygon points="0,0 541,0 473,142 0,142" fill="#ffffff"/>
    <polygon points="513,0 530,0 462,142 445,142" fill="#f07a18"/>
    <polygon points="541,0 564,0 496,142 473,142" fill="#e11b2b"/>
  </svg>
  <div class="brand">
    <span class="brand-mark"></span>
    <span class="brand-name">QUINLEY FORGE</span>
  </div>
  <p class="side-tagline">WHERE A TRADITION OF<br>GREAT PACKAGING MEETS<br>TOMORROW'S INNOVATIONS.</p>
</section>

<section class="door door-left" aria-label="Left back door">
  <div class="door-field"></div>
  <div class="door-brand">
    <span class="brand-mark"></span>
    <span class="brand-name">QUINLEY FORGE</span>
  </div>
  <p class="pride-note">We are very proud<br>of our sustainability<br>efforts</p>
</section>

<section class="door door-right" aria-label="Right back door">
  <div class="door-field"></div>
  <svg class="door-art" viewBox="0 0 326 760" width="326" height="760" aria-hidden="true">
    <polygon points="50,504 326,504 326,760 0,760 0,590" fill="#ffffff"/>
    <polygon points="38,504 48,504 4,574 0,574 0,566" fill="#e11b2b"/>
  </svg>
  <h2 class="products-title"><span class="big">OUR CORE</span><span class="small">PRODUCTS</span></h2>
  <ul class="product-list">
    <li><span class="product-icon"><svg viewBox="0 0 24 24"><path d="M12 2 21 7v10l-9 5-9-5V7z M3 7l9 5 9-5 M12 12v10" fill="none" stroke="#fff" stroke-width="2.4" stroke-linejoin="round"/></svg></span>Packaging</li>
    <li><span class="product-icon"><svg viewBox="0 0 24 24"><rect x="3" y="4" width="18" height="14" rx="2" fill="none" stroke="#fff" stroke-width="2.4"/><path d="M9 22h6M12 18v4" stroke="#fff" stroke-width="2.4"/></svg></span>Displays</li>
    <li><span class="product-icon"><svg viewBox="0 0 24 24"><path d="M12 2 20 5v7c0 5-4 9-8 10-4-1-8-5-8-10V5z" fill="#fff"/><path d="M8 12l3 3 5-6" fill="none" stroke="#e11b2b" stroke-width="2.4"/></svg></span>Protective</li>
    <li><span class="product-icon"><svg viewBox="0 0 24 24"><path d="M2 4h3l3 11h11l2-8H7" fill="none" stroke="#fff" stroke-width="2.4" stroke-linejoin="round"/><circle cx="9" cy="20" r="2" fill="#fff"/><circle cx="18" cy="20" r="2" fill="#fff"/></svg></span>E commerce</li>
  </ul>
  <p class="power-claim"><span class="lead">WE ARE</span><span class="figure">100%</span><span class="tail">POWERED</span></p>
</section>

</body>
</html>
```